Magazine Ad for TuneHaven School of Music

This will be an ad for music lessons. Logo and text are included in sections below. It will be used for print in newspapers and magazines, so it must look good in black & white as well as in color.

We need an 8.5" x 11" magazine ad (full page), also a 8.5" x 5.5" ad (half page), a 4.25" x 5.5" ad (quarter page) and a business card size ad.

Target Market(s)

Active mothers with children

Industry/Entity Type

School

Font styles to use
Serif

Requirements
Must have
• Must use one of the company logos (see uploaded files).
• All these ads should include the following text:
• ______________
• Music lessons in the comfort of YOUR HOUSE with EXPERIENCED and professional staff.
• Piano, Guitar, voice, VIOLIN, Drums, songwriting, and others
• Email contact@tunehavenlessons.org or call 508-647-3052
• www.TuneHavenLessons.org
• ______________
• The ad must look stylish and sharp in both color and black & white.

```html
<!DOCTYPE html>
<html lang="en">
<head>
<meta charset="utf-8">
<title>TuneHaven School of Music – Magazine Ad</title>
<link rel="stylesheet" href="https://fonts.googleapis.com/css2?family=Josefin+Sans:wght@300;400;700&display=swap">
<style>
  :root {
    --slate-dark: #1c1c1c;
    --slate-mid: #4a4a4a;
    --slate-light: #6e6e6e;
    --sun-yellow: #fcc62a;
    --fold-orange: #f6ab2a;
    --ink-black: #111111;
    --paper-white: #ffffff;
    --lesson-yellow: #f7c52c;
  }
  * { margin: 0; padding: 0; box-sizing: border-box; }
  html, body { width: 927px; height: 1200px; overflow: hidden; background: var(--slate-dark); }
  .ad {
    position: relative;
    width: 927px;
    height: 1200px;
    overflow: hidden;
    font-family: "Josefin Sans", "Century Gothic", sans-serif;
    background: radial-gradient(ellipse at 40% 55%, var(--slate-light) 0%, var(--slate-mid) 45%, var(--slate-dark) 100%);
  }
  .banner { position: absolute; inset: 0; width: 927px; height: 1200px; }
  .headline-band {
    position: absolute;
    left: 0; top: 510px;
    width: 927px; height: 220px;
    background: rgba(255,255,255,.12);
  }
  .guitar-photo {
    position: absolute;
    left: 700px; top: 20px;
    width: 227px; height: 1180px;
    background: linear-gradient(180deg, #c79a62 0%, #e2c08c 35%, #1a1a1a 55%, #e8e8e8 75%, #111 100%);
    clip-path: polygon(115px 0, 227px 0, 227px 1180px, 0 1180px, 0 625px, 115px 625px);
    opacity: .9;
  }
  .brand {
    position: absolute;
    left: 30px; top: 82px;
    display: flex; align-items: center; gap: 22px;
    color: var(--ink-black);
    z-index: 2;
  }
  .brand-mark {
    width: 252px; height: 252px;
    border-radius: 50%;
    background: var(--ink-black);
    flex: none;
  }
  .brand-name { line-height: 1; font-weight: 700; }
  .brand-name .primary { display: block; font-size: 84px; letter-spacing: -1px; }
  .brand-name .secondary { display: block; font-size: 36px; font-weight: 400; margin-top: 18px; padding-left: 88px; }
  .headline {
    position: absolute;
    left: 62px; top: 542px;
    color: var(--paper-white);
    font-weight: 700;
    text-transform: uppercase;
    text-shadow: 4px 4px 0 rgba(0,0,0,.55);
    line-height: 1.14;
    white-space: nowrap;
    z-index: 2;
  }
  .headline .line { display: block; font-size: 40px; letter-spacing: -.5px; }
  .headline .line.mid { font-size: 41px; }
  .headline .line.strong { font-size: 51px; padding-left: 12px; margin-top: 4px; }
  .lessons {
    position: absolute;
    left: 40px; top: 822px;
    color: var(--lesson-yellow);
    font-weight: 300;
    font-size: 35px;
    text-transform: uppercase;
    line-height: 1.3;
    letter-spacing: -.5px;
    white-space: nowrap;
    z-index: 2;
  }
  .lessons .row-first { display: block; padding-left: 44px; }
  .lessons .row-second { display: block; }
  .contact {
    position: absolute;
    left: 0; top: 990px;
    width: 700px;
    color: var(--paper-white);
    font-weight: 700;
    font-style: normal;
    line-height: 1;
    z-index: 2;
  }
  .contact-item { display: flex; align-items: center; gap: 8px; position: absolute; white-space: nowrap; }
  .contact-phone { left: 192px; top: 0; font-size: 40px; }
  .contact-email { left: 58px; top: 55px; font-size: 35px; }
  .contact-web { left: 80px; top: 105px; font-size: 40px; }
  .contact-item svg { fill: var(--paper-white); flex: none; }
</style>
</head>
<body>
<main class="ad">
  <svg class="banner" viewBox="0 0 927 1200" aria-hidden="true">
    <polygon points="0,45 880,45 880,380 0,400" fill="var(--sun-yellow)"/>
    <polygon points="0,400 470,392 470,420 0,500" fill="var(--fold-orange)"/>
  </svg>

  <div class="headline-band"></div>

  <div class="guitar-photo" role="img" aria-label="Photo of a black electric guitar with a maple neck standing upright"></div>

  <div class="brand">
    <span class="brand-mark"></span>
    <h1 class="brand-name">
      <span class="primary">TuneHaven</span>
      <span class="secondary">School of Music</span>
    </h1>
  </div>

  <h2 class="headline">
    <span class="line">Music lessons in the comfort of</span>
    <span class="line mid">your house with experienced</span>
    <span class="line strong">and professional staff.</span>
  </h2>

  <p class="lessons">
    <span class="row-first">Piano • Guitar &nbsp;Voice • Violin</span>
    <span class="row-second">Drums • Songwriting • And others</span>
  </p>

  <address class="contact">
    <span class="contact-item contact-phone">
      <svg width="36" height="36" viewBox="0 0 24 24" aria-hidden="true"><path d="M6.6 10.8a15.1 15.1 0 0 0 6.6 6.6l2.2-2.2a1 1 0 0 1 1-.25 11.4 11.4 0 0 0 3.6.57 1 1 0 0 1 1 1V20a1 1 0 0 1-1 1A17 17 0 0 1 3 4a1 1 0 0 1 1-1h3.5a1 1 0 0 1 1 1c0 1.25.2 2.45.57 3.57a1 1 0 0 1-.25 1z"/></svg>
      508-647-3052
    </span>
    <span class="contact-item contact-email">
      <svg width="36" height="26" viewBox="0 0 24 17" aria-hidden="true"><path d="M0 0h24v17H0z M1.5 1.5l10.5 8 10.5-8" stroke="#444" stroke-width="1.2" fill="var(--paper-white)"/></svg>
      contact@tunehavenlessons.org
    </span>
    <span class="contact-item contact-web">www.TuneHavenLessons.org</span>
  </address>
</main>
</body>
</html>
```